Consulting company, design, Interior design in commercial real estate (Tertiai sector *

Company name: DORALYNE: from the Greek Evexia well-being, was born from a desire to combine well-being and work. By the choice of design, materials, design and furniture, everything is thought from this perspective

Logo: Essay with Möbius Ribbon and / or with the infinite acronym / and or triangle ...
Sentences to write:
"The exclusive partner for your development projects"
"Consulting - Design - Construction"
"We manage EVERYTHING for you"

On the back: Photo (attached; if photo is not clear, another photo can be provided) with company name and "DORALYNE, Excellence and reliability"
My name / First name: provided later (double name), Manager
Address: supplied later
Tel: supplied later
Website: www. doralyne.example
Colors: Black, gold and white. Other admissible colors
See attached files

Target Market(s)

Real estate business

Contact Information for Business Card

Nom de l'entreprise : DORALYNE : du grec Evexia bien être, est né d'une volonté de faire rimer bien être et travail. Par le choix de la conception, des matériaux, du design et du mobilier, tout est pensé dans cette optique

Logo : Essai avec Ruban de Möbius et /ou avec le sigle infini / et ou triangle...
Phrases à inscrire :
"Le partenaire exclusif de vos projets d'aménagement"
"Conseil - Conception - Construction"
"Nous gérons TOUT pour vous"

Au verso : Photo (ci-jointe ; si photo pas nette, une autre photo peut être fournie) avec nom de l'entreprise et Mention "DORALYNE, Excellence et fiabilité"
Mon nom / Prénom : fourni ultérieurement (prénom double), Gérant
Adresse : fourni ultérieurement
Tél : fourni ultérieurement
Site Web : www. doralyne.example
Couleurs : Noir, doré et blanc. Autre couleurs recevables
Voir fichiers ci-joint

Requirements
Must have
• My project must be simple, clear, neat and design.
The business card must catch the customer

```html
<!DOCTYPE html>
<html lang="en">
<head>
<meta charset="utf-8">
<title>DORALYNE Business Card</title>
<link rel="stylesheet" href="https://fonts.googleapis.com/css2?family=Michroma&family=Oswald:wght@400;500;600&family=Poppins:wght@300;400&display=swap">
<style>
  :root {
    --bg: #1c1c1c;
    --card: #0b0b0b;
    --gold: #e3b52a;
    --gold-deep: #c9971c;
    --white: #ffffff;
    --soft: #e8e8e8;
  }
  * { margin: 0; padding: 0; box-sizing: border-box; }
  html, body { width: 1200px; height: 900px; overflow: hidden; background: var(--bg); }
  .stage { position: relative; width: 1200px; height: 900px; }
  .card {
    position: absolute; left: 250px; width: 700px; height: 400px;
    background: var(--card);
    box-shadow: 0 14px 30px rgba(0,0,0,.55);
  }
  .card--front { top: 30px; }
  .card--back { top: 470px; }

  .brand { display: flex; flex-direction: column; align-items: center; }
  .brand__row { display: flex; align-items: center; gap: 12px; }
  .brand__mark { width: 14px; height: 14px; background: var(--gold); }
  .brand__name {
    font-family: "Michroma", sans-serif; color: var(--white);
    font-size: 34px; letter-spacing: 2px; line-height: 1;
  }
  .brand__tagline {
    display: flex; align-items: center; gap: 8px; margin-top: 8px;
    font-family: "Poppins", sans-serif; font-size: 11px; color: var(--gold);
    letter-spacing: 1px; text-transform: uppercase;
  }
  .brand__tagline::before, .brand__tagline::after {
    content: ""; width: 22px; height: 1px; background: var(--gold);
  }

  .front__brand { position: absolute; top: 92px; left: 0; right: 0; }
  .front__copy { position: absolute; top: 220px; left: 0; right: 0; text-align: center; font-family: "Oswald", sans-serif; color: var(--white); }
  .front__lead { font-size: 17px; font-weight: 500; letter-spacing: .5px; }
  .front__services { font-size: 30px; font-weight: 600; letter-spacing: 1px; margin-top: 2px; }
  .front__promise { font-size: 14px; font-weight: 500; margin-top: 22px; letter-spacing: .5px; }

  .back__brand { position: absolute; top: 48px; left: 54px; width: 290px; }
  .back__brand .brand__name { font-size: 28px; }
  .back__rule { position: absolute; left: 250px; right: 0; top: 160px; height: 1px; background: var(--gold-deep); }
  .person { position: absolute; left: 60px; top: 186px; }
  .person__name { font-family: "Michroma", sans-serif; color: var(--white); font-size: 24px; letter-spacing: 1px; }
  .person__role { font-family: "Poppins", sans-serif; color: var(--soft); font-size: 16px; margin-top: 2px; }
  .contact {
    position: absolute; left: 60px; top: 270px; width: 270px;
    border-top: 1px solid var(--gold-deep); padding-top: 12px;
    font-family: "Poppins", sans-serif; color: var(--white); font-size: 17px;
  }
  .contact__item { display: flex; align-items: center; gap: 10px; line-height: 26px; }
  .contact__icon { width: 15px; height: 15px; fill: var(--gold); flex: none; }
  .contact__end { position: absolute; left: 60px; top: 372px; width: 270px; height: 1px; background: var(--gold-deep); }
  .address {
    position: absolute; right: 44px; top: 178px; text-align: right;
    font-family: "Poppins", sans-serif; color: var(--white); font-size: 16px; line-height: 22px;
  }
</style>
</head>
<body>
<main class="stage">
  <section class="card card--front">
    <div class="brand front__brand">
      <div class="brand__row"><span class="brand__mark"></span><span class="brand__name">DORALYNE</span></div>
      <div class="brand__tagline">Excellence and reliability</div>
    </div>
    <div class="front__copy">
      <p class="front__lead">THE EXCLUSIVE PARTNER FOR YOUR DEVELOPMENT PROJECTS</p>
      <p class="front__services">CONSULTING - DESIGN - CONSTRUCTION</p>
      <p class="front__promise">WE MANAGE EVERYTHING FOR YOU</p>
    </div>
  </section>

  <section class="card card--back">
    <div class="brand back__brand">
      <div class="brand__row"><span class="brand__mark"></span><span class="brand__name">DORALYNE</span></div>
      <div class="brand__tagline">Excellence and reliability</div>
    </div>
    <div class="back__rule"></div>
    <div class="person">
      <p class="person__name">ALDEN MARSH</p>
      <p class="person__role">Executive Director</p>
    </div>
    <div class="contact">
      <p class="contact__item">
        <svg class="contact__icon" viewBox="0 0 24 24"><path d="M6.6 10.8a15 15 0 0 0 6.6 6.6l2.2-2.2a1 1 0 0 1 1-.25 11.4 11.4 0 0 0 3.6.57 1 1 0 0 1 1 1V20a1 1 0 0 1-1 1A17 17 0 0 1 3 4a1 1 0 0 1 1-1h3.5a1 1 0 0 1 1 1c0 1.25.2 2.45.57 3.57a1 1 0 0 1-.25 1z"/></svg>
        000-000-0000
      </p>
      <p class="contact__item">
        <svg class="contact__icon" viewBox="0 0 24 24"><path d="M2 5h20v14H2zm2 2v.5l8 5 8-5V7l-8 5z"/></svg>
        alden@marsh.example
      </p>
      <p class="contact__item">
        <svg class="contact__icon" viewBox="0 0 24 24"><path d="M12 2a10 10 0 1 0 0 20 10 10 0 0 0 0-20zm6.9 9h-3a15 15 0 0 0-1.3-5.6A8 8 0 0 1 18.9 11zM12 4c.9 1.2 1.7 3.6 1.9 7h-3.8c.2-3.4 1-5.8 1.9-7zM9.4 5.4A15 15 0 0 0 8.1 11h-3a8 8 0 0 1 4.3-5.6zM5.1 13h3a15 15 0 0 0 1.3 5.6A8 8 0 0 1 5.1 13zm6.9 7c-.9-1.2-1.7-3.6-1.9-7h3.8c-.2 3.4-1 5.8-1.9 7zm2.6-1.4a15 15 0 0 0 1.3-5.6h3a8 8 0 0 1-4.3 5.6z"/></svg>
        www.doralyne.example
      </p>
    </div>
    <div class="contact__end"></div>
    <p class="address">00000 Harrow Lane, Suite 000<br>Westbrook Hill, ON, L0C 000</p>
  </section>
</main>
</body>
</html>
```